Cold brew coffee concept

Web site/logo for cold brew coffee served in a keg tap. Cold brew coffee is a natural energy beverage roasted with fair trade/organic beans. Based in New England. Think- Fresh, Natural, Organic, Pure, Mills, Brick, Wood. Ferncastle Coldbrew.

Target Market(s)

Individuals looking for energy drinks without added sugar or dairy. Coffee connoisseurs.

Industry/Entity Type

Trade

Logo Text

Ferncastle Coldbrew

Number of Pages Required

1 page

Font styles to use
Serif

```html
<!DOCTYPE html>
<html lang="en">
<head>
<meta charset="utf-8">
<title>Ferncastle Coldbrew</title>
<link href="https://fonts.googleapis.com/css2?family=Raleway:ital,wght@0,400;0,600;0,700;0,800;1,400&display=swap" rel="stylesheet">
<style>
:root{
  --gold:#fdb813;
  --ink:#3a2a1e;
  --body:#5a5a5a;
  --wood:#6e3610;
  --wood-dark:#582a0b;
  --footer:#4a3c31;
  --white:#ffffff;
  --input:#e6e6e6;
}
*{box-sizing:border-box;margin:0;padding:0}
html,body{width:1200px;height:3502px;overflow:hidden}
body{font-family:"Raleway",sans-serif;color:var(--body);background:var(--white);position:relative}
.btn{display:inline-block;background:var(--gold);color:var(--white);font-weight:700;font-size:15px;text-transform:uppercase;padding:0 34px;height:46px;line-height:46px;letter-spacing:.3px}
.rule{width:68px;height:3px;background:var(--gold);margin:0 auto}
.section-title{font-weight:800;color:var(--ink);font-size:34px;text-transform:uppercase;text-align:center;letter-spacing:.5px}

/* hero */
.hero{position:absolute;left:0;top:0;width:1200px;height:658px;background:linear-gradient(180deg,#2b231d 0%,#5b4a3c 35%,#7a6b5e 55%,#3b2f26 100%)}
.topbar{position:absolute;left:0;top:0;width:1200px;height:128px;background:rgba(20,16,12,.55);border-bottom:1px solid rgba(255,255,255,.35)}
.social-top{position:absolute;left:76px;top:32px;display:flex;gap:19px}
.social-top span,.social-foot span{width:15px;height:15px;border-radius:50%;background:var(--white);display:block}
.utility{position:absolute;right:70px;top:30px;display:flex;gap:30px}
.brand{position:absolute;left:0;width:1200px;top:32px;text-align:center;color:var(--white);font-weight:800;font-size:36px;text-transform:uppercase;letter-spacing:1px}
.nav{position:absolute;left:0;top:128px;width:1200px;height:48px;background:rgba(10,8,6,.6);display:flex;justify-content:center;align-items:center;gap:58px;border-bottom:1px solid rgba(255,255,255,.25)}
.nav a{color:var(--white);text-decoration:none;font-weight:700;font-size:13px;text-transform:uppercase}
.nav a.active{color:var(--gold)}
.hero-text{position:absolute;left:0;top:325px;width:1200px;text-align:center;color:var(--white)}
.hero-text h1{font-weight:800;font-size:54px;text-transform:uppercase;letter-spacing:1px}
.hero-text p{font-weight:700;font-size:35px;margin-top:2px}
.hero-text .btn{margin-top:20px}
.arrow{position:absolute;top:375px}

/* welcome */
.welcome{position:absolute;left:0;top:658px;width:1200px;height:350px;text-align:center;padding-top:32px}
.welcome .rule{margin-top:20px}
.welcome p{width:1050px;margin:24px auto 0;font-size:14px;line-height:24px}
.welcome .btn{margin-top:40px}

/* split features */
.feature{position:absolute;left:0;width:1200px;display:flex}
.photo{width:600px;height:100%}
.panel{width:600px;height:100%;background:repeating-linear-gradient(90deg,var(--wood) 0 7px,var(--wood-dark) 7px 9px,var(--wood) 9px 19px);color:var(--white);padding:46px 42px 0}
.panel h2{font-weight:800;font-size:31px;text-transform:uppercase;letter-spacing:.5px}
.panel p{font-size:14px;line-height:24px;margin-top:26px;width:520px}
.panel .btn{margin-top:30px}

/* shop */
.shop{position:absolute;left:0;top:1405px;width:1200px;height:373px;background:linear-gradient(160deg,#2a3038 0%,#49525c 45%,#1f242a 100%);text-align:center;color:var(--white);padding-top:66px}
.shop h2{font-weight:800;font-size:31px;text-transform:uppercase}
.shop .rule{margin-top:12px}
.shop p{width:960px;margin:22px auto 0;font-size:14px;line-height:24px}
.shop .btn{margin-top:34px}

/* testimonials */
.testimonials{position:absolute;left:0;top:2176px;width:1200px;height:481px;text-align:center;padding-top:40px}
.testimonials .rule{margin-top:20px}
.testimonials blockquote{width:1060px;margin:46px auto 0;font-style:italic;font-size:14px;line-height:24px}
.q{color:var(--gold);font-weight:800;font-style:normal}
.name{margin-top:24px;color:var(--gold);font-weight:700;font-size:13px;text-transform:uppercase}
.location{font-style:italic;font-size:13px;margin-top:6px}
.avatar-row{display:flex;justify-content:center;align-items:center;gap:42px;margin-top:18px}
.avatar{width:126px;height:126px;border-radius:50%;background:radial-gradient(circle at 50% 40%,#b8554a 0%,#7d2a26 60%,#5a2a22 100%)}

/* newsletter */
.newsletter{position:absolute;left:0;top:3058px;width:1200px;height:262px;text-align:center;padding-top:32px}
.newsletter p{font-size:15px;margin-top:42px}
.signup{display:flex;justify-content:center;gap:14px;margin-top:32px}
.signup .field{width:390px;height:47px;background:var(--input);text-align:left;padding-left:16px;line-height:47px;font-size:13px;color:#8a8a8a}
.signup .btn{width:152px;padding:0;height:47px;line-height:47px}

/* footer */
.footer{position:absolute;left:0;top:3320px;width:1200px;height:182px;background:var(--footer);color:#d8cfc6}
.foot-brand{position:absolute;left:77px;top:46px;font-weight:800;font-size:24px;text-transform:uppercase;color:var(--white)}
.legal{position:absolute;left:77px;top:100px;font-size:11px;line-height:19px;text-transform:uppercase}
.contact{position:absolute;left:642px;top:46px}
.foot-head{font-weight:700;font-size:15px;text-transform:uppercase;color:var(--white)}
.phone{color:var(--gold);font-weight:800;font-size:27px;margin-top:10px}
.email{font-size:13px;margin-top:8px}
.connect{position:absolute;left:934px;top:46px}
.social-foot{display:flex;gap:20px;margin-top:24px}
</style>
</head>
<body>

<header class="hero" role="img" aria-label="Espresso machine pouring coffee into white cups, warm blurred café background">
  <div class="topbar">
    <div class="social-top"><span></span><span></span><span></span><span></span><span></span><span></span></div>
    <div class="brand">Ferncastle Coldbrew</div>
    <div class="utility">
      <svg width="16" height="16" viewBox="0 0 16 16"><circle cx="8" cy="5" r="3.5" fill="#fff"/><path d="M1 16c0-4 3-6 7-6s7 2 7 6z" fill="#fff"/></svg>
      <svg width="18" height="16" viewBox="0 0 18 16"><path d="M0 1h3l2 9h10l2-7H5" fill="none" stroke="#fff" stroke-width="2"/><circle cx="6" cy="14" r="1.6" fill="#fff"/><circle cx="14" cy="14" r="1.6" fill="#fff"/></svg>
      <svg width="16" height="16" viewBox="0 0 16 16"><circle cx="6.5" cy="6.5" r="5" fill="none" stroke="#fff" stroke-width="2"/><path d="M10 10l5 5" stroke="#fff" stroke-width="2.4"/></svg>
    </div>
  </div>
  <nav class="nav">
    <a class="active" href="#">Home</a><a href="#">About Us</a><a href="#">Our Coffee</a><a href="#">Shop</a><a href="#">Blog</a><a href="#">News</a><a href="#">Testimonials</a><a href="#">Contact Us</a>
  </nav>
  <svg class="arrow" style="left:56px" width="24" height="38" viewBox="0 0 24 38"><path d="M20 3L5 19l15 16" fill="none" stroke="#fff" stroke-width="4"/></svg>
  <svg class="arrow" style="right:56px" width="24" height="38" viewBox="0 0 24 38"><path d="M4 3l15 16L4 35" fill="none" stroke="#fff" stroke-width="4"/></svg>
  <div class="hero-text">
    <h1>Ferncastle Coldbrew</h1>
    <p>We sell cold brew coffee served in a keg tap</p>
    <a class="btn" href="#">Read More</a>
  </div>
</header>

<section class="welcome">
  <h2 class="section-title">Welcome to Ferncastle Coldbrew</h2>
  <div class="rule"></div>
  <p>Aliquam molestie, mi et imperdiet euismod, dui purus auctor tellus, et interdum lacus lectus et ante. Sed accumsan sollicitudin sapien, sit amet adipiscing turpis gravida ac. In congue, neque ac lobortis volutpat, libero mauris varius mi, vitae suscipit ipsum ligula vitae risus. Duis aliquam nibh a dui iaculis viverra id a velit. Vivamus egestas risus in magna varius commodo. Sed semper viverra egestas. Etiam pretium porttitor lectus, vel ornare neque porta volutpat.</p>
  <a class="btn" href="#">Read More</a>
</section>

<section class="feature" style="top:1008px;height:397px">
  <div class="photo" role="img" aria-label="Iced cold brew in a glass with cinnamon sticks on scattered coffee beans" style="background:radial-gradient(circle at 45% 45%,#c79a6a 0%,#7a4a28 40%,#3a2415 100%)"></div>
  <div class="panel">
    <h2>Cold Brew Coffee</h2>
    <p>Aliquam molestie, mi et imperdiet euismod, dui purus auctor tellus, et interdum lacus lectus et ante. Sed accumsan sollicitudin sapien, sit amet adipiscing turpis gravida ac. In congue, neque ac lobortis volutpat, libero mauris varius mi, vitae suscipit ipsum ligula vitae risus. Duis aliquam nibh a dui iaculis viverra id a velit.</p>
    <a class="btn" href="#">Read More</a>
  </div>
</section>

<section class="shop" role="img" aria-label="Dark background of a coffee machine and glass jug">
  <h2>Shop</h2>
  <div class="rule"></div>
  <p>Aliquam molestie, mi et imperdiet euismod, dui purus auctor tellus, et interdum lacus lectus et ante. Sed accumsan sollicitudin sapien, sit amet adipiscing turpis gravida ac.</p>
  <a class="btn" href="#">Visit Our Store</a>
</section>

<section class="feature" style="top:1778px;height:398px">
  <div class="panel">
    <h2>Roasted Fair Coffee</h2>
    <p>Aliquam molestie, mi et imperdiet euismod, dui purus auctor tellus, et interdum lacus lectus et ante. Sed accumsan sollicitudin sapien, sit amet adipiscing turpis gravida ac. In congue, neque ac lobortis volutpat, libero mauris varius mi, vitae suscipit ipsum ligula vitae risus. Duis aliquam nibh a dui iaculis viverra id a velit.</p>
    <a class="btn" href="#">Read More</a>
  </div>
  <div class="photo" role="img" aria-label="Burlap sack of roasted coffee beans with fresh green mint leaves" style="background:radial-gradient(circle at 60% 45%,#e6dccb 0%,#8a6a3e 35%,#4a2c14 100%)"></div>
</section>

<section class="testimonials">
  <h2 class="section-title">What Our Customers Says..</h2>
  <div class="rule"></div>
  <blockquote><span class="q">&ldquo;</span> Aliquam molestie, mi et imperdiet euismod, dui purus auctor tellus, et interdum lacus lectus et ante. Sed accumsan sollicitudin sapien, sit amet adipiscing turpis gravida ac. In congue, neque ac lobortis volutpat, libero mauris varius mi, vitae suscipit ipsum ligula vitae risus. Duis aliquam nibh a dui iaculis viverra id a velit. Vivamus egestas risus in magna varius commodo... <span class="q">&rdquo;</span></blockquote>
  <div class="name">Name Heading</div>
  <div class="location">Location</div>
  <div class="avatar-row">
    <svg width="14" height="22" viewBox="0 0 14 22"><path d="M12 2L3 11l9 9" fill="none" stroke="#999" stroke-width="2.5"/></svg>
    <div class="avatar" role="img" aria-label="Portrait of a customer holding a red coffee cup"></div>
    <svg width="14" height="22" viewBox="0 0 14 22"><path d="M2 2l9 9-9 9" fill="none" stroke="#999" stroke-width="2.5"/></svg>
  </div>
</section>

<section class="feature" style="top:2657px;height:401px">
  <div class="photo" role="img" aria-label="Three friends outdoors holding takeaway coffee cups" style="background:linear-gradient(135deg,#e9e4d8 0%,#c9b59a 40%,#7fa38a 75%,#d6cfc2 100%)"></div>
  <div class="panel">
    <h2>Tasty Coffee</h2>
    <p>Aliquam molestie, mi et imperdiet euismod, dui purus auctor tellus, et interdum lacus lectus et ante. Sed accumsan sollicitudin sapien, sit amet adipiscing turpis gravida ac. In congue, neque ac lobortis volutpat, libero mauris varius mi, vitae suscipit ipsum ligula vitae risus. Duis aliquam nibh a dui iaculis viverra id a velit.</p>
    <a class="btn" href="#">Read More</a>
  </div>
</section>

<section class="newsletter">
  <h2 class="section-title">Newsletter Sign Up</h2>
  <p>Aliquam molestie, mi et imperdiet euismod, dui purus auctor tellus, et interdum lacus lectus et ante.</p>
  <div class="signup">
    <div class="field">Enter Email Address</div>
    <a class="btn" href="#">Sign Up</a>
  </div>
</section>

<footer class="footer">
  <div class="foot-brand">Ferncastle Coldbrew</div>
  <div class="legal">Copyright © 2016. All right reserved. Terms &amp; Conditions<br>Privacy Policy | Terms of Uses</div>
  <div class="contact">
    <div class="foot-head">Contact Info</div>
    <div class="phone">1-800-555-0142</div>
    <div class="email">hello@ferncastlecoldbrew.com</div>
  </div>
  <div class="connect">
    <div class="foot-head">Connect Us</div>
    <div class="social-foot"><span></span><span></span><span></span><span></span><span></span><span></span></div>
  </div>
</footer>

</body>
</html>
```